Educational Management System User Interface (Veltrix Design Concepts)

Hi,I require a 1-page design for an educational management system. The image attached shows all required elements and also their locations. I require the design to be based on veltrix-styled interfaces using elements from: http://pramel.examplehost.io/pramel-framekit/ & http://kitnulloa.com/kitnulloa-layout/admin . Side menu's should not be too large that they hide the main content of the page.
Sorry very slight addition to the design as per new uploaded file.
I like how the elements of the veltrix orbit page are seperated with the background colour and white boxes. This could maybe work in the design as per the uploaded image?
Thanks,
Tobias
Reason: Some designers have some submissions.

```html
<!DOCTYPE html>
<html lang="en">
<head>
<meta charset="utf-8">
<title>Norvane LMS – Group Feed</title>
<link rel="stylesheet" href="https://fonts.googleapis.com/css2?family=Roboto:wght@400;500;700&display=swap">
<style>
:root{
  --topbar:#2e2e2e;
  --sidebar:#2a2a2a;
  --sidebar-band:#202020;
  --sidebar-line:#3d3d3d;
  --feed-bg:#ececec;
  --aside-bg:#dcdcdc;
  --aside-band:#cfcfcf;
  --aside-line:#bdbdbd;
  --card:#ffffff;
  --card-line:#d6d6d6;
  --toolbar:#f3f3f3;
  --text:#333333;
  --text-light:#ffffff;
  --muted:#8a8a8a;
  --icon-grey:#7a7a7a;
  --icon-pale:#c9c9c9;
  --blue:#6c88b8;
  --green:#49b64c;
  --green-soft:#5fc46b;
  --red:#e14a35;
  --timeline:#cfcfcf;
}
*{box-sizing:border-box;margin:0;padding:0}
html,body{width:1200px;height:1043px;overflow:hidden}
body{font-family:"Roboto",Arial,sans-serif;color:var(--text);background:var(--feed-bg);position:relative;font-size:12.5px}

/* top bar */
.topbar{position:absolute;left:0;top:0;width:1200px;height:65px;background:var(--topbar)}
.brand{position:absolute;left:24px;top:20px;font-size:21px;font-weight:500;color:var(--text-light)}
.main-nav{position:absolute;left:224px;top:17px;display:flex;gap:14px}
.main-nav svg{width:32px;height:32px;display:block}
.user-tools{position:absolute;right:22px;top:12px;display:flex;align-items:center}
.tool{position:relative;width:32px;height:32px;margin-right:10px}
.tool svg{width:30px;height:30px}
.badge{position:absolute;right:-3px;bottom:-3px;width:15px;height:15px;border-radius:50%;background:var(--green);color:#fff;font-size:9px;font-weight:700;text-align:center;line-height:15px}
.user-name{color:var(--text-light);font-size:12.5px;font-weight:500;margin:0 16px 0 14px}
.user-photo{width:40px;height:40px;border-radius:50%;background:radial-gradient(circle at 50% 40%,#2f4757,#10161c)}

/* sidebar */
.sidebar{position:absolute;left:0;top:65px;width:201px;height:978px;background:var(--sidebar);color:var(--text-light)}
.role{height:58px;background:var(--sidebar-band);text-align:center;line-height:58px;font-size:13px;font-weight:500}
.side-title{text-align:center;font-size:13px;font-weight:500;margin-top:20px;margin-bottom:6px}
.side-list{list-style:none;margin:0 22px}
.side-list li{height:40px;display:flex;align-items:center;justify-content:space-between;border-bottom:1px solid var(--sidebar-line);font-size:12px}
.side-list li.is-dim{color:#8b8b8b}
.go{width:14px;height:14px}
.side-btn{display:block;margin:0 22px;height:26px;border-radius:2px;color:#fff;font-size:12px;font-weight:500;text-align:center;line-height:26px}
.btn-green{background:var(--green);margin-top:22px}
.btn-blue{background:var(--blue);margin-top:9px}
.side-divider{height:1px;background:var(--sidebar-line);margin-top:23px}

/* feed */
.avatar{position:absolute;width:65px;height:65px;border-radius:50%;background:linear-gradient(150deg,#c9b48a 0%,#3d5670 55%,#22303e 100%);border:2px solid #fff}
.avatar.small{width:47px;height:47px;background:linear-gradient(160deg,#7b4a34 0%,#e6c2a6 55%,#f1f1f1 100%)}
.timeline{position:absolute;left:258px;top:150px;width:2px;height:520px;background:var(--timeline)}
.composer{position:absolute;left:313px;top:88px;width:587px}
.composer-input{height:56px;background:var(--card);padding:13px 12px;font-size:12px}
.composer-bar{height:57px;margin-top:2px;background:var(--toolbar);border:1px solid #e0e0e0;display:flex;align-items:center;justify-content:flex-end;padding-right:15px;gap:14px}
.composer-bar svg{width:30px;height:30px}
.submit{width:157px;height:26px;background:var(--blue);color:#fff;border-radius:2px;font-size:12px;font-weight:500;text-align:center;line-height:26px;margin-left:12px}
.refresh{position:absolute;left:224px;top:203px;width:66px;height:64px}

.post{position:absolute;background:var(--card);border:1px solid var(--card-line);padding:13px 12px}
.post-head{font-size:12px;margin-bottom:13px}
.post-head b{font-weight:500;font-size:13px}
.post-head .sep{margin:0 5px}
.post-body{font-size:12px;line-height:18px;max-width:510px}
.reply{position:absolute;right:14px;bottom:16px;width:28px;height:24px}
.post.with-file{padding-left:94px}
.file{position:absolute;left:14px;top:12px;width:60px;text-align:center;font-size:11px;font-weight:700}
.file svg{width:56px;height:66px;display:block;margin:0 auto 14px}
.thread-v{position:absolute;left:336px;top:808px;width:2px;height:36px;background:var(--timeline)}
.thread-h{position:absolute;left:360px;top:866px;width:39px;height:2px;background:var(--timeline)}

/* events */
.events{position:absolute;left:922px;top:65px;width:278px;height:978px;background:var(--aside-bg)}
.events-head{height:58px;background:var(--aside-band);display:flex;align-items:center;justify-content:center;gap:8px;font-size:13px;font-weight:500}
.events-head svg{width:26px;height:28px}
.event-list{list-style:none;margin:4px 22px 0 22px}
.event-list li{height:40px;display:flex;align-items:center;justify-content:space-between;border-bottom:1px solid var(--aside-line);font-size:12px}
.event-list b{font-weight:500}
.info{width:14px;height:14px}
.events-head.upcoming{margin-top:23px}
</style>
</head>
<body>

<header class="topbar">
  <div class="brand">Norvane LMS</div>
  <nav class="main-nav">
    <svg viewBox="0 0 32 32" aria-label="Home"><path d="M16 4 2 17h4v11h8v-8h4v8h8V17h4z" fill="var(--icon-grey)"/></svg>
    <svg viewBox="0 0 32 32" aria-label="Calendar"><rect x="4" y="6" width="24" height="22" fill="none" stroke="var(--icon-grey)" stroke-width="3"/><rect x="4" y="6" width="24" height="6" fill="var(--icon-grey)"/><g fill="var(--icon-grey)"><rect x="8" y="15" width="4" height="3"/><rect x="14" y="15" width="4" height="3"/><rect x="20" y="15" width="4" height="3"/><rect x="8" y="21" width="4" height="3"/><rect x="14" y="21" width="4" height="3"/><rect x="20" y="21" width="4" height="3"/></g></svg>
    <svg viewBox="0 0 32 32" aria-label="Tasks"><path d="M3 17l4-4 6 6L26 6l4 4-17 17z" fill="var(--green)"/></svg>
    <svg viewBox="0 0 32 32" aria-label="Files"><path d="M2 8h10l3 3h13v4H8L2 27z" fill="var(--icon-grey)"/><path d="M9 16h22l-6 12H3z" fill="var(--icon-grey)"/></svg>
  </nav>
  <div class="user-tools">
    <div class="tool"><svg viewBox="0 0 30 30" aria-label="Mentions"><circle cx="15" cy="15" r="12" fill="none" stroke="var(--blue)" stroke-width="3"/><circle cx="15" cy="15" r="5" fill="none" stroke="var(--blue)" stroke-width="3"/><path d="M20 11v6a3 3 0 0 0 6 0" fill="none" stroke="var(--blue)" stroke-width="3"/></svg><span class="badge">3</span></div>
    <div class="tool"><svg viewBox="0 0 30 30" aria-label="Notifications"><path d="M15 4c-5 0-8 4-8 9v6l-3 4h22l-3-4v-6c0-5-3-9-8-9z" fill="var(--red)"/><circle cx="15" cy="26" r="3" fill="var(--red)"/></svg><span class="badge">6</span></div>
    <span class="user-name">Marla Fennick</span>
    <div class="user-photo" role="img" aria-label="Profile photo of Marla Fennick"></div>
  </div>
</header>

<aside class="sidebar">
  <div class="role">TEACHER</div>
  <h2 class="side-title">MY GROUPS</h2>
  <ul class="side-list">
    <li>Groupname one<svg class="go" viewBox="0 0 14 14"><circle cx="7" cy="7" r="6" fill="none" stroke="#888" stroke-width="1.3"/><path d="M4 7h6M7.5 4.5 10 7 7.5 9.5" fill="none" stroke="#888" stroke-width="1.3"/></svg></li>
    <li class="is-dim">Groupname two<svg class="go" viewBox="0 0 14 14"><circle cx="7" cy="7" r="6" fill="none" stroke="var(--red)" stroke-width="1.3"/><path d="M4 7h6M7.5 4.5 10 7 7.5 9.5" fill="none" stroke="var(--red)" stroke-width="1.3"/></svg></li>
    <li>Groupname three<svg class="go" viewBox="0 0 14 14"><circle cx="7" cy="7" r="6" fill="none" stroke="#888" stroke-width="1.3"/><path d="M4 7h6M7.5 4.5 10 7 7.5 9.5" fill="none" stroke="#888" stroke-width="1.3"/></svg></li>
    <li>Groupname four<svg class="go" viewBox="0 0 14 14"><circle cx="7" cy="7" r="6" fill="none" stroke="#888" stroke-width="1.3"/><path d="M4 7h6M7.5 4.5 10 7 7.5 9.5" fill="none" stroke="#888" stroke-width="1.3"/></svg></li>
  </ul>
  <a class="side-btn btn-green">Create new Group</a>
  <a class="side-btn btn-blue">Join more Groups</a>
  <div class="side-divider"></div>
  <h2 class="side-title">COMMUNITY</h2>
  <ul class="side-list">
    <li>Learn Nook<svg class="go" viewBox="0 0 14 14"><circle cx="7" cy="7" r="6" fill="none" stroke="#888" stroke-width="1.3"/><path d="M4 7h6M7.5 4.5 10 7 7.5 9.5" fill="none" stroke="#888" stroke-width="1.3"/></svg></li>
  </ul>
</aside>

<main>
  <div class="timeline"></div>
  <div class="avatar" style="left:224px;top:88px" role="img" aria-label="Profile photo of the teacher"></div>
  <section class="composer">
    <div class="composer-input">Your message here and post it</div>
    <div class="composer-bar">
      <svg viewBox="0 0 30 30" aria-label="Add photo"><path d="M3 9h6l2-3h8l2 3h6v16H3z" fill="var(--icon-pale)"/><circle cx="15" cy="16" r="5" fill="#fff"/><circle cx="15" cy="16" r="3" fill="var(--icon-pale)"/></svg>
      <svg viewBox="0 0 30 30" aria-label="Add document"><circle cx="15" cy="15" r="13" fill="var(--icon-pale)"/><path d="M11 8h6l3 3v11h-9z" fill="#fff"/></svg>
      <svg viewBox="0 0 30 30" aria-label="Attach file"><path d="M20 8 10 18a3 3 0 0 0 4 4l11-11a5 5 0 0 0-7-7L7 15a7 7 0 0 0 10 10l7-7" fill="none" stroke="var(--icon-pale)" stroke-width="2.5" stroke-linecap="round"/></svg>
      <span class="submit">Submit my post now</span>
    </div>
  </section>

  <svg class="refresh" viewBox="0 0 66 64" aria-label="Refresh feed"><path d="M33 12a20 20 0 1 0 20 20h-10a10 10 0 1 1-10-10v8l16-13L33 4z" fill="var(--green-soft)"/></svg>

  <div class="avatar" style="left:224px;top:310px" role="img" aria-label="Profile photo of Idris Pellow"></div>
  <article class="post" style="left:313px;top:310px;width:587px;height:143px">
    <p class="post-head"><b>Idris Pellow</b><span class="sep">|</span>09:15 14/05/2014</p>
    <p class="post-body">Lorem ipsum dolor sit amet, consectetur adipiscing elit. Etiam sagittis neque et pharetra hendrerit. Suspendisse potenti. Nulla congue massa non eros accumsan placerat. Nullam bibendum odio sem, vel varius purus viverra nec. Morbi eleifend, arcu vel mattis</p>
    <svg class="reply" viewBox="0 0 28 24" aria-label="Reply"><path d="M11 2 1 11l10 9v-6c7 0 12 2 16 8-1-9-6-15-16-15z" fill="var(--icon-pale)"/></svg>
  </article>

  <div class="avatar" style="left:224px;top:476px" role="img" aria-label="Profile photo of Idris Pellow"></div>
  <article class="post" style="left:313px;top:476px;width:587px;height:142px">
    <p class="post-head"><b>Idris Pellow</b><span class="sep">|</span>09:15 14/05/2014</p>
    <p class="post-body">Integer et vulputate est. In scelerisque lectus enim, at luctus neque pretium eget. Proin nec pellentesque enim. Pellentesque odio leo, vulputate nec risus quis, vulputate mollis ex.</p>
    <svg class="reply" viewBox="0 0 28 24" aria-label="Reply"><path d="M11 2 1 11l10 9v-6c7 0 12 2 16 8-1-9-6-15-16-15z" fill="var(--icon-pale)"/></svg>
  </article>

  <div class="avatar" style="left:224px;top:642px" role="img" aria-label="Profile photo of Idris Pellow"></div>
  <article class="post with-file" style="left:313px;top:642px;width:587px;height:142px">
    <div class="file">
      <svg viewBox="0 0 56 66" aria-label="PDF file"><path d="M8 2h30l14 14v48H8z" fill="#fff" stroke="var(--red)" stroke-width="4"/><path d="M38 2v14h14" fill="none" stroke="var(--red)" stroke-width="4"/><rect x="0" y="10" width="40" height="22" fill="var(--red)"/><text x="20" y="26" text-anchor="middle" font-family="Roboto,Arial,sans-serif" font-size="14" font-weight="700" fill="#fff">PDF</text></svg>
      result.pdf
    </div>
    <p class="post-head"><b>Idris Pellow</b><span class="sep">|</span>09:15 14/05/2014</p>
    <p class="post-body" style="max-width:420px">Integer et vulputate est. In scelerisque lectus enim, at luctus neque pretium eget. Proin nec pellentesque enim. Pellentesque odio leo, vulputate nec risus quis, vulputate mollis ex.</p>
    <svg class="reply" viewBox="0 0 28 24" aria-label="Reply"><path d="M11 2 1 11l10 9v-6c7 0 12 2 16 8-1-9-6-15-16-15z" fill="var(--icon-pale)"/></svg>
  </article>

  <div class="thread-v"></div>
  <div class="thread-h"></div>
  <div class="avatar small" style="left:314px;top:843px" role="img" aria-label="Profile photo of a student"></div>
  <article class="post" style="left:420px;top:808px;width:480px;height:142px">
    <p class="post-head"><b>Idris Pellow</b><span class="sep">|</span>09:15 14/05/2014</p>
    <p class="post-body" style="max-width:420px">Integer et vulputate est. In scelerisque lectus enim, at luctus neque pretium eget. Proin nec pellentesque enim. Pellentesque odio leo, vulputate nec risus quis, vulputate mollis ex.</p>
    <svg class="reply" viewBox="0 0 28 24" aria-label="Reply"><path d="M11 2 1 11l10 9v-6c7 0 12 2 16 8-1-9-6-15-16-15z" fill="var(--icon-pale)"/></svg>
  </article>
</main>

<aside class="events">
  <h2 class="events-head"><svg viewBox="0 0 26 28"><rect x="1" y="4" width="24" height="23" fill="var(--red)"/><rect x="5" y="1" width="3" height="6" fill="var(--red)"/><rect x="18" y="1" width="3" height="6" fill="var(--red)"/><rect x="1" y="9" width="24" height="1.5" fill="#fff"/><text x="13" y="24" text-anchor="middle" font-family="Roboto,Arial,sans-serif" font-size="12" font-weight="700" fill="#fff">31</text></svg>TODAY'S EVENTS</h2>
  <ul class="event-list">
    <li><span><b>12:15am</b> Meeting in the canteen</span><svg class="info" viewBox="0 0 14 14"><circle cx="7" cy="7" r="7" fill="var(--blue)"/><rect x="6" y="6" width="2" height="5" fill="#fff"/><rect x="6" y="3" width="2" height="2" fill="#fff"/></svg></li>
    <li><span><b>12:15am</b> Meeting in the canteen</span><svg class="info" viewBox="0 0 14 14"><circle cx="7" cy="7" r="7" fill="var(--blue)"/><rect x="6" y="6" width="2" height="5" fill="#fff"/><rect x="6" y="3" width="2" height="2" fill="#fff"/></svg></li>
    <li><span><b>12:15am</b> Meeting in the canteen</span><svg class="info" viewBox="0 0 14 14"><circle cx="7" cy="7" r="7" fill="var(--blue)"/><rect x="6" y="6" width="2" height="5" fill="#fff"/><rect x="6" y="3" width="2" height="2" fill="#fff"/></svg></li>
    <li><span><b>12:15am</b> Meeting in the canteen</span><svg class="info" viewBox="0 0 14 14"><circle cx="7" cy="7" r="7" fill="var(--blue)"/><rect x="6" y="6" width="2" height="5" fill="#fff"/><rect x="6" y="3" width="2" height="2" fill="#fff"/></svg></li>
    <li><span><b>12:15am</b> Meeting in the canteen</span><svg class="info" viewBox="0 0 14 14"><circle cx="7" cy="7" r="7" fill="var(--blue)"/><rect x="6" y="6" width="2" height="5" fill="#fff"/><rect x="6" y="3" width="2" height="2" fill="#fff"/></svg></li>
  </ul>
  <h2 class="events-head upcoming"><svg viewBox="0 0 26 28"><rect x="1" y="4" width="24" height="23" fill="var(--red)"/><rect x="5" y="1" width="3" height="6" fill="var(--red)"/><rect x="18" y="1" width="3" height="6" fill="var(--red)"/><rect x="1" y="9" width="24" height="1.5" fill="#fff"/><text x="13" y="24" text-anchor="middle" font-family="Roboto,Arial,sans-serif" font-size="12" font-weight="700" fill="#fff">31</text></svg>UPCOMING EVENTS</h2>
  <ul class="event-list">
    <li><span><b>12:15am</b> Meeting in the canteen</span><svg class="info" viewBox="0 0 14 14"><circle cx="7" cy="7" r="7" fill="var(--blue)"/><rect x="6" y="6" width="2" height="5" fill="#fff"/><rect x="6" y="3" width="2" height="2" fill="#fff"/></svg></li>
    <li><span><b>12:15am</b> Meeting in the canteen</span><svg class="info" viewBox="0 0 14 14"><circle cx="7" cy="7" r="7" fill="var(--blue)"/><rect x="6" y="6" width="2" height="5" fill="#fff"/><rect x="6" y="3" width="2" height="2" fill="#fff"/></svg></li>
    <li><span><b>12:15am</b> Meeting in the canteen</span><svg class="info" viewBox="0 0 14 14"><circle cx="7" cy="7" r="7" fill="var(--blue)"/><rect x="6" y="6" width="2" height="5" fill="#fff"/><rect x="6" y="3" width="2" height="2" fill="#fff"/></svg></li>
  </ul>
</aside>

</body>
</html>
```